Bag packaging design of sliced bread

The project is for design of line of sliced bread with different flavours. The brand of the bread will be "Valorina". The shape of the bread will be oval. The bread will be packed in a bag. I attach the layout of the bag. The bag will be closed with a plastic clip. I attach images of similar products. The idea is to have one main design and then each colour to be different type of bread like those in the images 2 and 5.

```html
<!DOCTYPE html>
<html lang="en">
<head>
<meta charset="utf-8">
<title>Valorina sliced bread – bag artwork</title>
<link rel="stylesheet" href="https://fonts.googleapis.com/css2?family=Oswald:wght@500;600;700&display=swap">
<style>
  :root{
    --bg-top:#dff7f6;
    --bg-bottom:#ffffff;
    --ribbon-dark:#6e1736;
    --ribbon-mid:#a3285a;
    --bow:#c2405f;
    --white:#ffffff;

    --orange-dark:#4a2a12;
    --orange-stripe:#f7a021;
    --orange-light:#fccd66;
    --orange-strip:#f7a021;
    --orange-head-text:#f7a021;

    --pink-dark:#ec008c;
    --pink-stripe:#ec008c;
    --pink-light:#f9d3e6;
    --pink-strip:#f28cc0;
    --pink-head-text:#f9d3e6;

    --green-dark:#179448;
    --green-stripe:#179448;
    --green-light:#d4e6d6;
    --green-strip:#7dc243;
    --green-head-text:#d4e6d6;
  }
  *{box-sizing:border-box;margin:0;padding:0}
  html,body{width:780px;height:1200px;overflow:hidden}
  body{
    position:relative;
    background:linear-gradient(var(--bg-top),var(--bg-bottom));
    font-family:"Oswald",sans-serif;
  }

  .flavour{position:absolute;width:232px}
  .flavour--orange{left:16px;--dark:var(--orange-dark);--stripe:var(--orange-stripe);--light:var(--orange-light);--strip:var(--orange-strip);--head-text:var(--orange-head-text)}
  .flavour--pink{left:274px;--dark:var(--pink-dark);--stripe:var(--pink-stripe);--light:var(--pink-light);--strip:var(--pink-strip);--head-text:var(--pink-head-text)}
  .flavour--green{left:532px;--dark:var(--green-dark);--stripe:var(--green-stripe);--light:var(--green-light);--strip:var(--green-strip);--head-text:var(--green-head-text)}

  .stripes{
    background:repeating-linear-gradient(90deg,var(--light) 0 13.6px,var(--stripe) 13.6px 27.2px);
  }

  /* front panel */
  .front-panel{position:absolute;top:330px;left:0;width:232px;height:335px}
  .front-panel .stripes{position:absolute;left:0;top:0;width:232px;height:221px}
  .header-band{
    position:absolute;left:0;top:0;width:232px;height:29px;
    background:var(--dark);
    display:flex;justify-content:space-around;align-items:center;
    color:var(--head-text);font-weight:600;font-size:11px;letter-spacing:.5px;
  }
  .header-rule{position:absolute;left:0;top:32px;width:232px;height:3px;background:var(--dark)}
  .ribbon-band{
    position:absolute;left:0;width:232px;height:22px;
    background:linear-gradient(var(--ribbon-mid),var(--ribbon-dark) 55%,var(--ribbon-mid));
  }
  .front-panel .ribbon-band{top:199px}
  .bow{
    position:absolute;left:52px;top:183px;width:128px;height:52px;
    border-radius:14px;
    background:linear-gradient(var(--bow),var(--ribbon-dark));
  }
  .mascot{
    position:absolute;left:85px;top:180px;width:62px;height:62px;border-radius:50%;
    background:radial-gradient(#ffffff 55%,#f4dcdc);
    border:2px solid #e8c7c7;
  }
  .label{
    position:absolute;left:72px;top:240px;width:88px;height:93px;
    background:var(--white);border:3px solid var(--dark);border-radius:8px;overflow:hidden;
    text-align:center;
  }
  .brand{
    position:absolute;left:0;top:244px;width:232px;text-align:center;
    font-weight:700;font-size:19px;color:var(--dark);line-height:1;
  }
  .label-title{
    margin-top:24px;font-weight:600;font-size:16px;line-height:16px;color:var(--dark);
  }
  .label-claim{font-family:"Oswald",sans-serif;font-weight:500;font-size:6px;color:var(--strip);margin-top:3px;letter-spacing:.3px}
  .label-weight{
    position:absolute;left:0;bottom:0;width:100%;height:18px;
    background:var(--strip);color:var(--white);font-weight:600;font-size:11px;line-height:18px;
  }

  /* back panel */
  .back-panel{position:absolute;top:722px;left:0;width:232px;height:130px}
  .back-panel .stripes{position:absolute;left:0;top:0;width:232px;height:130px}
  .back-panel .ribbon-band{top:0}
</style>
</head>
<body>
  <section class="flavour flavour--orange">
    <div class="front-panel">
      <div class="stripes"></div>
      <div class="header-band"><span>Valorina</span><span>Valorina</span><span>Valorina</span></div>
      <div class="header-rule"></div>
      <div class="ribbon-band"></div>
      <div class="bow" role="img" aria-label="Satin ribbon bow"></div>
      <div class="mascot" role="img" aria-label="Baker mascot badge"></div>
      <div class="label">
        <p class="label-title">WHOLE<br>WHEAT</p>
        <p class="label-claim">100% NATURALA</p>
        <p class="label-weight">500gr</p>
      </div>
      <p class="brand">Valorina</p>
    </div>
    <div class="back-panel">
      <div class="stripes"></div>
      <div class="ribbon-band"></div>
    </div>
  </section>

  <section class="flavour flavour--pink">
    <div class="front-panel">
      <div class="stripes"></div>
      <div class="header-band"><span>Valorina</span><span>Valorina</span><span>Valorina</span></div>
      <div class="header-rule"></div>
      <div class="ribbon-band"></div>
      <div class="bow" role="img" aria-label="Satin ribbon bow"></div>
      <div class="mascot" role="img" aria-label="Baker mascot badge"></div>
      <div class="label">
        <p class="label-title">WHOLE<br>WHEAT</p>
        <p class="label-claim" style="color:var(--dark)">100% NATURALA</p>
        <p class="label-weight">500gr</p>
      </div>
      <p class="brand">Valorina</p>
    </div>
    <div class="back-panel">
      <div class="stripes"></div>
      <div class="ribbon-band"></div>
    </div>
  </section>

  <section class="flavour flavour--green">
    <div class="front-panel">
      <div class="stripes"></div>
      <div class="header-band"><span>Valorina</span><span>Valorina</span><span>Valorina</span></div>
      <div class="header-rule"></div>
      <div class="ribbon-band"></div>
      <div class="bow" role="img" aria-label="Satin ribbon bow"></div>
      <div class="mascot" role="img" aria-label="Baker mascot badge"></div>
      <div class="label">
        <p class="label-title">WHOLE<br>WHEAT</p>
        <p class="label-claim" style="color:var(--dark)">100% NATURALA</p>
        <p class="label-weight">500gr</p>
      </div>
      <p class="brand">Valorina</p>
    </div>
    <div class="back-panel">
      <div class="stripes"></div>
      <div class="ribbon-band"></div>
    </div>
  </section>
</body>
</html>
```